Blueprints For A Steady Home Book*

Our book is about using engineering and biblical principles to solve problems in marriage. We are the wedlock Architects. See our branded logo in the attachments. We would like to see different types of graphics that shows continuous improvement in marriage. Our colors should be Gold Black and Red. Could use white text and symbols if needed. Brief description on the back with some quotes and our Picture. Use 5.5x8.5 as the size of the book. Not sure about the spine size.

Target Market(s)

Married couples

Font styles to use
Serif

Colors

Designer to choose colors to be used in the design.

Requirements
Nice to have
• Engineering symbols and Logos.

```html
<!DOCTYPE html>
<html lang="en">
<head>
<meta charset="utf-8">
<title>Blueprints For A Steady Home Book – Cover</title>
<link href="https://fonts.googleapis.com/css2?family=Marcellus&display=swap" rel="stylesheet">
<style>
  :root {
    --page-bg: #f4f4f4;
    --cover-black: #000000;
    --title-gold: #f2a619;
    --rule-red: #c8101a;
    --heart-red: #d8141c;
    --heart-deep: #8e0a10;
    --ring-gold-light: #f7d27a;
    --ring-gold-mid: #c9922a;
    --ring-gold-dark: #7a5312;
  }
  * { margin: 0; padding: 0; box-sizing: border-box; }
  html, body {
    width: 1200px;
    height: 800px;
    overflow: hidden;
    background: var(--page-bg);
  }
  .canvas {
    position: relative;
    width: 1200px;
    height: 800px;
  }
  .book-cover {
    position: absolute;
    left: 367px;
    top: 40px;
    width: 466px;
    height: 720px;
    background: var(--cover-black);
    overflow: hidden;
  }
  .heart-band {
    position: absolute;
    left: 14px;
    right: 14px;
    height: 66px;
    background:
      radial-gradient(ellipse at 12% 50%, var(--heart-red) 0 10%, transparent 40%),
      radial-gradient(ellipse at 38% 45%, var(--heart-red) 0 10%, transparent 40%),
      radial-gradient(ellipse at 62% 55%, var(--heart-red) 0 10%, transparent 40%),
      radial-gradient(ellipse at 88% 50%, var(--heart-red) 0 10%, transparent 40%),
      linear-gradient(90deg, var(--heart-deep), #5a0408 50%, var(--heart-deep));
    opacity: 0.9;
    border-radius: 6px;
  }
  .heart-band--top { top: 16px; }
  .heart-band--bottom { top: 638px; }
  .red-rule {
    position: absolute;
    left: 18px;
    right: 18px;
    height: 2px;
    background: var(--rule-red);
  }
  .red-rule--top { top: 100px; }
  .red-rule--bottom { top: 620px; }
  .cover-title {
    position: absolute;
    top: 132px;
    left: 0;
    right: 0;
    text-align: center;
    font-family: "Marcellus", serif;
    font-weight: 400;
    color: var(--title-gold);
    text-transform: uppercase;
    line-height: 1;
  }
  .cover-title .title-line {
    display: block;
    font-size: 50px;
    letter-spacing: -1px;
    margin-bottom: 26px;
  }
  .cover-title .title-line--book {
    font-size: 64px;
  }
  .cover-title .title-small {
    font-size: 38px;
  }
  .rings-art {
    position: absolute;
    left: 84px;
    top: 448px;
    width: 296px;
    height: 160px;
    border-radius: 80px;
    background: radial-gradient(ellipse at 45% 40%, var(--ring-gold-light), var(--ring-gold-mid) 45%, var(--ring-gold-dark) 75%, var(--cover-black) 100%);
  }
</style>
</head>
<body>
  <main class="canvas">
    <section class="book-cover">
      <div class="heart-band heart-band--top" role="img" aria-label="Scattered red hearts border"></div>
      <div class="red-rule red-rule--top"></div>

      <h1 class="cover-title">
        <span class="title-line">Blueprints</span>
        <span class="title-line"><span class="title-small">For a</span> Steady</span>
        <span class="title-line">Home</span>
        <span class="title-line title-line--book">Book</span>
      </h1>

      <div class="rings-art" role="img" aria-label="Two interlocked gold wedding rings"></div>

      <div class="red-rule red-rule--bottom"></div>
      <div class="heart-band heart-band--bottom" role="img" aria-label="Scattered red hearts border"></div>
    </section>
  </main>
</body>
</html>
```